Buisness Card for an Agricultural Contracting and Earthmoving Company

We need a business card for a new business based in Kilmore, Victoria. We are a company that specialises in two areas the first is and Earthmoving company, we do large jobs such as soccer fields to small jobs such as house cuts and riding arena's, drainage, and dams. The other side of the business specialises in Agricultural improvements and hay contracting. We require a card to represent both sides of the business. Must have the following information: Dale Morcombe, 2741 Bracken Rd, Brackenvale Victoria 3799, ph:03 5902 4638, mob: 0427 913 684, e-mail: dale@morcombeworks.com.au. Earthmoving and Agricultural Contracting.

Target Market(s)

Builder's, Council's, new home buyers, Farmers

Industry/Entity Type

House

Font styles to use
Sans Serif

Colors
ec2026
000000
5c5c5c
ffffff

Requirements
Must have
• Both facets of the business represented. Company logo

```html
<!DOCTYPE html>
<html lang="en">
<head>
<meta charset="utf-8">
<title>Morcombe Contracting – Business Card</title>
<link rel="stylesheet" href="https://fonts.googleapis.com/css2?family=Arimo:wght@400;700&family=Tinos:wght@700&display=swap">
<style>
  :root {
    --brand-red: #ec2026;
    --ink: #000000;
    --card-dark: #1a0c0c;
    --card-maroon: #3a1414;
    --muted-grey: #5c5c5c;
    --contact-grey: #a9a9a9;
    --white: #ffffff;
  }
  * { box-sizing: border-box; margin: 0; padding: 0; }
  html, body { width: 1066px; height: 1200px; overflow: hidden; background: var(--white); }
  .canvas { position: relative; width: 1066px; height: 1200px; background: var(--white); }

  .card {
    position: absolute; left: 98px; width: 869px; height: 473px; overflow: hidden;
    background: linear-gradient(160deg, #3b3b3b 0%, var(--card-dark) 40%, var(--card-maroon) 100%);
  }
  .card--front { top: 67px; }
  .card--back { top: 659px; background: linear-gradient(180deg, var(--card-maroon) 0%, var(--card-dark) 45%, #2a2a2a 100%); }
  .card__swoosh { position: absolute; inset: 0; width: 100%; height: 100%; }

  .brand__mark { position: absolute; background: var(--brand-red); }
  .brand__name {
    position: absolute; text-align: center;
    font-family: "Arimo", Arial, sans-serif; font-weight: 700; color: var(--brand-red);
    text-transform: uppercase; letter-spacing: 1px; white-space: nowrap; line-height: 1;
  }
  .card--front .brand__mark { left: 126px; top: 27px; width: 94px; height: 94px; }
  .card--front .brand__name { left: 0; width: 344px; top: 147px; font-size: 19.5px; }
  .card--back .brand__mark { left: 372px; top: 40px; width: 125px; height: 125px; }
  .card--back .brand__name { left: 0; right: 0; top: 204px; font-size: 27px; }

  .person { position: absolute; left: 0; width: 344px; top: 248px; text-align: center; }
  .person__name {
    font-family: "Tinos", "Times New Roman", serif; font-weight: 700; font-size: 43px; line-height: 50px;
    color: var(--white); text-shadow: 0 2px 4px var(--ink);
  }
  .person__role {
    font-family: "Arimo", Arial, sans-serif; font-weight: 700; font-size: 30px; line-height: 36px;
    color: var(--muted-grey); margin-top: 0;
  }

  .contact { position: absolute; right: 35px; top: 196px; list-style: none; }
  .contact__item {
    display: flex; align-items: center; justify-content: flex-end; gap: 22px;
    font-family: "Arimo", Arial, sans-serif; font-size: 28px; color: var(--contact-grey);
    text-align: right; line-height: 33px;
  }
  .contact__item--phone { margin-top: 10px; }
  .contact__item--mobile { margin-top: 15px; }
  .contact__item--email { margin-top: 9px; }
  .contact__icon { width: 38px; height: 38px; flex: none; }

  .tagline {
    position: absolute; left: 0; right: 0; top: 240px; text-align: center;
    font-family: "Arimo", Arial, sans-serif; font-weight: 700; font-size: 29.5px; line-height: 36px;
    color: var(--white); text-shadow: 0 2px 4px var(--ink);
  }
</style>
</head>
<body>
<main class="canvas">
  <svg width="0" height="0" style="position:absolute">
    <defs>
      <radialGradient id="icon-fill" cx="40%" cy="35%" r="70%">
        <stop offset="0" stop-color="#ff5a5f"/>
        <stop offset="0.6" stop-color="#ec2026"/>
        <stop offset="1" stop-color="#8a0d12"/>
      </radialGradient>
      <linearGradient id="swoosh-red" x1="0" y1="0" x2="1" y2="0">
        <stop offset="0" stop-color="#ec2026" stop-opacity="0"/>
        <stop offset="0.5" stop-color="#ec2026" stop-opacity="0.55"/>
        <stop offset="1" stop-color="#ff8a80" stop-opacity="0.9"/>
      </linearGradient>
      <linearGradient id="swoosh-red-back" x1="1" y1="0" x2="0" y2="0">
        <stop offset="0" stop-color="#ec2026" stop-opacity="0"/>
        <stop offset="0.5" stop-color="#ec2026" stop-opacity="0.5"/>
        <stop offset="1" stop-color="#ff7a70" stop-opacity="0.9"/>
      </linearGradient>
    </defs>
  </svg>

  <section class="card card--front" aria-label="Business card front">
    <svg class="card__swoosh" viewBox="0 0 869 473" preserveAspectRatio="none" aria-hidden="true">
      <path d="M0 0 H869 V50 C640 70 420 210 0 170 Z" fill="url(#swoosh-red)" opacity="0.75"/>
      <path d="M0 175 C420 215 640 80 869 55" stroke="#ff4a4f" stroke-width="3" fill="none" opacity="0.8"/>
      <path d="M0 190 C430 228 650 110 869 95" stroke="#ec2026" stroke-width="1.5" fill="none" opacity="0.5"/>
    </svg>

    <div class="brand__mark"></div>
    <div class="brand__name">Morcombe Contracting</div>

    <div class="person">
      <div class="person__name">Dale Morcombe</div>
      <div class="person__role">Director</div>
    </div>

    <ul class="contact">
      <li class="contact__item contact__item--address">
        <span>2741 Bracken Rd,<br>Brackenvale Victoria 3799</span>
        <svg class="contact__icon" viewBox="0 0 40 40" aria-hidden="true"><circle cx="20" cy="20" r="19" fill="url(#icon-fill)"/><path d="M9 20 L20 10 L31 20 H28 V30 H23 V24 H17 V30 H12 V20 Z" fill="#fff"/></svg>
      </li>
      <li class="contact__item contact__item--phone">
        <span>03 5902 4638</span>
        <svg class="contact__icon" viewBox="0 0 40 40" aria-hidden="true"><circle cx="20" cy="20" r="19" fill="url(#icon-fill)"/><path d="M9 17 Q20 9 31 17 L29 20 L25 18 L25 16 Q20 14 15 16 L15 18 L11 20 Z" fill="#fff"/><path d="M13 22 H27 L29 29 H11 Z" fill="#fff"/><circle cx="20" cy="25" r="2" fill="#ec2026"/></svg>
      </li>
      <li class="contact__item contact__item--mobile">
        <span>0427 913 684</span>
        <svg class="contact__icon" viewBox="0 0 40 40" aria-hidden="true"><circle cx="20" cy="20" r="19" fill="url(#icon-fill)"/><rect x="13" y="8" width="14" height="24" rx="2" fill="#fff"/><rect x="15" y="11" width="10" height="16" fill="#ec2026"/><circle cx="20" cy="29.5" r="1.3" fill="#ec2026"/></svg>
      </li>
      <li class="contact__item contact__item--email">
        <span>dale@morcombeworks.com.au</span>
        <svg class="contact__icon" viewBox="0 0 40 40" aria-hidden="true"><circle cx="20" cy="20" r="19" fill="url(#icon-fill)"/><rect x="9" y="13" width="22" height="15" fill="#fff"/><path d="M9 13 L20 22 L31 13" stroke="#ec2026" stroke-width="1.5" fill="none"/></svg>
      </li>
    </ul>
  </section>

  <section class="card card--back" aria-label="Business card back">
    <svg class="card__swoosh" viewBox="0 0 869 473" preserveAspectRatio="none" aria-hidden="true">
      <path d="M0 473 H869 V300 C620 290 380 410 0 425 Z" fill="url(#swoosh-red-back)" opacity="0.7"/>
      <path d="M0 410 C380 400 620 285 869 298" stroke="#ff4a4f" stroke-width="3" fill="none" opacity="0.8"/>
      <path d="M0 445 C400 428 640 325 869 340" stroke="#ec2026" stroke-width="1.5" fill="none" opacity="0.5"/>
    </svg>

    <div class="brand__mark"></div>
    <div class="brand__name">Morcombe Contracting</div>

    <p class="tagline">Earthmoving and Agricultural Contracting</p>
  </section>
</main>
</body>
</html>
```